Brisca Coffee Cups

We already have Brisca Coffee cups, but the existing design is dated.
It needs a fresh modern look. (this look will be used with all Brisca advertising..
But the look and font of the word Brisca needs to say the same.

Industry/Entity Type

Advertising

```html
<!DOCTYPE html>
<html lang="en">
<head>
<meta charset="utf-8">
<title>Brisca Coffee Cup Wrap</title>
<link href="https://fonts.googleapis.com/css2?family=Open+Sans:wght@600&display=swap" rel="stylesheet">
<style>
  :root {
    --page: #ffffff;
    --wrap-tan: #8c7456;
    --frame-dark: #1a1108;
    --bean-dark: #2a170b;
    --bean-mid: #5a3a26;
    --bean-light: #8a7a78;
    --text-light: #ffffff;
  }
  html, body {
    margin: 0;
    padding: 0;
    width: 1200px;
    height: 989px;
    overflow: hidden;
    background: var(--page);
  }
  .canvas {
    position: relative;
    width: 1200px;
    height: 989px;
    font-family: "Open Sans", sans-serif;
  }
  .cup-wrap {
    position: absolute;
    left: 65px;
    top: 105px;
    width: 1078px;
    height: 782px;
    background: var(--wrap-tan);
    border: 1.5px solid var(--frame-dark);
  }
  .inner-frame {
    position: absolute;
    left: 35px;
    top: 40px;
    width: 1000px;
    height: 700px;
    border: 4px solid var(--frame-dark);
  }
  .bean-art {
    position: absolute;
    left: 279px;
    top: 88px;
    width: 470px;
    height: 420px;
  }
  .brand-name {
    position: absolute;
    left: 0;
    width: 1078px;
    top: 212px;
    margin: 0;
    text-align: center;
    font-size: 118px;
    font-weight: 600;
    line-height: 1;
    letter-spacing: 2px;
    color: var(--text-light);
  }
  .brand-descriptor {
    position: absolute;
    left: 0;
    width: 1078px;
    top: 338px;
    margin: 0;
    text-align: center;
    font-size: 44px;
    font-weight: 600;
    line-height: 1;
    letter-spacing: 2px;
    color: var(--text-light);
  }
  .web-address {
    position: absolute;
    left: 0;
    width: 1078px;
    top: 700px;
    margin: 0;
    text-align: center;
    font-size: 22px;
    font-weight: 600;
    letter-spacing: 0.5px;
    color: var(--text-light);
  }
</style>
</head>
<body>
  <div class="canvas">
    <div class="cup-wrap">
      <div class="inner-frame"></div>
      <svg class="bean-art" viewBox="0 0 470 420" role="img" aria-label="Illustration of a roasted coffee bean">
        <defs>
          <radialGradient id="beanTone" cx="50%" cy="45%" r="60%">
            <stop offset="0%" stop-color="#2a170b"/>
            <stop offset="70%" stop-color="#5a3a26"/>
            <stop offset="100%" stop-color="#6f5650"/>
          </radialGradient>
        </defs>
        <ellipse cx="235" cy="210" rx="232" ry="205" transform="rotate(12 235 210)" fill="url(#beanTone)" stroke="var(--frame-dark)" stroke-width="6"/>
      </svg>
      <h1 class="brand-name">Brisca</h1>
      <p class="brand-descriptor">CAFFE</p>
      <p class="web-address">www.brewcupprints.com.au</p>
    </div>
  </div>
</body>
</html>
```